Cedar Ridge Lakemont Dining Fortnight

We need our flyer from last year updated. Please use this year's logo, attached below and use a similar overall layout as last year's flyer, which is also attached. The goal is to make this year's flyer less cluttered.

1. Remove the cornucopia/food background, and instead incorporate an attractive table, wine glass(es) and possibly a wine bottle.

2. Include this year's logo, attached, prominently in the middle of the flyer, possibly larger.

3. Take out the prices and the 4 buttons/circles with the price options all together.

4. Include the logos for Lantern Fair and the Cedar Ridge Civic Quarter (with the fountain), attached.

The website should be changed to: CRLDiningFortnight.example

```html
<!DOCTYPE html>
<html lang="en">
<head>
<meta charset="utf-8">
<title>Cedar Ridge Lakemont Dining Fortnight – Flyer</title>
<link href="https://fonts.googleapis.com/css2?family=Roboto:wght@400;500;700&display=swap" rel="stylesheet">
<style>
  :root {
    --page-bg: #ecebe9;
    --coral: #e8474a;
    --coral-deep: #d63b3f;
    --maroon: #5a1a1d;
    --ink: #3a1a1b;
    --mist-top: #b9b6c6;
    --mist-bottom: #ffffff;
    --white: #ffffff;
    --teal: #2a9aa6;
    --plum: #6a3a7a;
  }
  * { margin: 0; padding: 0; box-sizing: border-box; }
  html, body { width: 1200px; height: 1000px; overflow: hidden; }
  body {
    background: var(--page-bg);
    font-family: "Roboto", Arial, sans-serif;
    position: relative;
  }
  .flyer {
    position: absolute;
    left: 333px; top: 62px;
    width: 533px; height: 880px;
    background: linear-gradient(to bottom, var(--mist-top) 30%, #dcdbe3 60%, var(--mist-bottom) 85%);
    overflow: hidden;
  }
  .table-photo {
    position: absolute; left: 0; top: 0;
    width: 533px; height: 300px;
    background:
      radial-gradient(ellipse at 20% 25%, #d9899b 0%, rgba(217,137,155,0) 40%),
      radial-gradient(ellipse at 78% 40%, #c9765a 0%, rgba(201,118,90,0) 35%),
      linear-gradient(to bottom, #b88a94 0%, #a8a0ad 55%, rgba(185,182,198,0) 100%);
  }
  .event-mark {
    position: absolute; left: 48px; top: 130px;
    width: 440px; height: 440px;
    border-radius: 50%;
    background: var(--coral);
    box-shadow: 0 0 0 14px var(--coral-deep) inset;
    display: flex; flex-direction: column; align-items: center; justify-content: center;
    color: var(--white); font-weight: 700; text-align: center;
  }
  .event-mark .line-small { font-size: 26px; letter-spacing: 1px; }
  .event-mark .line-mid { font-size: 44px; margin-top: 14px; }
  .event-mark .line-large { font-size: 70px; line-height: 1; }
  .event-dates {
    position: absolute; left: 0; top: 582px; width: 533px;
    text-align: center; font-size: 22px; font-weight: 700; color: var(--coral-deep);
  }
  .host {
    position: absolute; left: 0; top: 620px; width: 533px; text-align: center; color: var(--ink);
  }
  .host-label { font-size: 14px; font-weight: 500; }
  .host-title { font-size: 19px; font-weight: 700; margin-top: 2px; }
  .host-name { font-size: 28px; font-weight: 700; color: var(--coral); margin-top: 2px; }
  .partners {
    position: absolute; left: 0; top: 725px; width: 533px;
    display: flex; justify-content: center; align-items: center; gap: 22px;
  }
  .partner { display: flex; align-items: center; gap: 8px; font-size: 15px; font-weight: 700; }
  .partner .dot { width: 16px; height: 16px; border-radius: 50%; }
  .partner--fair { color: var(--teal); }
  .partner--fair .dot { background: var(--teal); }
  .partner--civic { color: var(--plum); }
  .partner--civic .dot { background: var(--plum); }
  .partner-divider { width: 2px; height: 60px; background: var(--maroon); }
  .web-band {
    position: absolute; left: 0; top: 804px; width: 533px; height: 30px;
    background: var(--coral);
    color: var(--maroon); font-size: 21px; font-weight: 700; letter-spacing: 0.5px;
    display: flex; align-items: center; justify-content: center;
  }
  .social-band {
    position: absolute; left: 0; top: 834px; width: 533px; height: 46px;
    background: var(--maroon);
    display: flex; align-items: center; justify-content: center; gap: 14px;
    color: var(--white); font-size: 10px;
  }
  .social { display: flex; align-items: center; gap: 5px; }
  .social .square { width: 20px; height: 20px; background: #d8d8d8; }
</style>
</head>
<body>
  <main class="flyer">
    <div class="table-photo" role="img" aria-label="Dinner table set with roses, glass decanters and glasses of rosé wine"></div>

    <div class="event-mark">
      <span class="line-small">CEDAR RIDGE LAKEMONT</span>
      <span class="line-mid">DINING</span>
      <span class="line-large">FORTNIGHT</span>
    </div>
    <div class="event-dates">September 6 – 11, 2016</div>

    <section class="host">
      <p class="host-label">Hosted by:</p>
      <p class="host-title">Harwell County Councilmember</p>
      <p class="host-name">Dana Whitfield</p>
    </section>

    <section class="partners">
      <div class="partner partner--fair"><span class="dot"></span>Lantern Fair</div>
      <div class="partner-divider"></div>
      <div class="partner partner--civic"><span class="dot"></span>Cedar Ridge Civic Quarter</div>
    </section>

    <div class="web-band">www.CRLDiningFortnight.example</div>
    <footer class="social-band">
      <span class="social"><span class="square"></span>cedarridgedining</span>
      <span class="social"><span class="square"></span>@CedarRidgeDF #CRDF</span>
      <span class="social"><span class="square"></span>@cedarridgedining</span>
    </footer>
  </main>
</body>
</html>
```